Online Charity Portal

We need a website mockup for a new project.

GivingSpark is a toolbar download that will donate a penny to your favorite charity for every search you perform. The website will be approximately 2-3 pages with the home page explaining the overall concept. One tab at the top will be FAQ's and other "Charities".

On the home page there needs to be a registration form that will collect Name, email, address, charity (from a pull down list of 20 charity names).

The site should be clean and neat with a very professional look and feel.

A site I really like and you can emulate is - https://profilenook.example/

Once completed - the code will be given to the backend developer to implement.

Industry/Entity Type

Charity

Requirements
Must have

```html
<!DOCTYPE html>
<html lang="en">
<head>
<meta charset="utf-8">
<title>giving spark</title>
<link rel="stylesheet" href="https://fonts.googleapis.com/css2?family=Open+Sans:wght@700&family=Questrial&display=swap">
<style>
  :root {
    --bar-black: #000000;
    --tab-grey: #333333;
    --tab-text: #ffffff;
    --brand-blue: #1c5f82;
    --ink: #111111;
    --panel-white: rgba(236, 241, 245, 0.88);
    --field-fill: #f1f9fd;
    --field-line: #1c5f82;
    --placeholder: #9aa3a8;
    --dot: #5e686d;
    --dot-active: #9a9fa2;
    --stone-light: #c9c6bf;
    --stone-mid: #8f8a82;
    --skin-brown: #6e5847;
    --cloth-grey: #9aa3a6;
    --wall-teal: #2c5767;
    --wall-deep: #122a35;
  }
  * { box-sizing: border-box; margin: 0; padding: 0; }
  html, body { width: 1200px; height: 900px; overflow: hidden; background: var(--bar-black); }
  .page { position: relative; width: 1200px; height: 900px; font-family: "Questrial", sans-serif; }

  .top-bar { position: absolute; left: 0; top: 0; width: 1200px; height: 58px; background: var(--bar-black); }
  .nav-tab {
    position: absolute; top: 15px; height: 30px; padding: 0 10px;
    background: var(--tab-grey); color: var(--tab-text); border-radius: 3px;
    font: 700 12px/30px "Open Sans", sans-serif; text-decoration: none;
  }
  .nav-faq { left: 867px; width: 59px; text-align: center; padding: 0; }
  .nav-charities { left: 939px; width: 83px; text-align: center; padding: 0; }

  .hero-photo {
    position: absolute; left: 0; top: 58px; width: 1200px; height: 842px;
    background:
      linear-gradient(180deg, rgba(0,0,0,0) 0%, rgba(0,0,0,0) 65%, rgba(40,38,36,0.35) 100%),
      linear-gradient(90deg,
        var(--stone-light) 0%,
        var(--stone-mid) 18%,
        var(--skin-brown) 30%,
        var(--cloth-grey) 42%,
        var(--skin-brown) 52%,
        var(--wall-teal) 66%,
        var(--wall-teal) 80%,
        var(--wall-deep) 100%);
  }

  .slider-dots { position: absolute; left: 1005px; top: 85px; display: flex; gap: 12px; }
  .slider-dot { width: 9px; height: 9px; background: var(--dot); }
  .slider-dot.is-active { background: var(--dot-active); }

  .signup-panel {
    position: absolute; left: 669px; top: 226px; width: 359px; height: 579px;
    background: var(--panel-white); border-radius: 3px;
  }
  .brand-name {
    position: absolute; left: 15px; top: 24px; white-space: nowrap;
    font-size: 58px; font-weight: 400; line-height: 1; color: var(--brand-blue); letter-spacing: -0.5px;
  }
  .tagline { position: absolute; left: 20px; top: 106px; font-size: 29px; font-weight: 400; color: var(--ink); letter-spacing: 0.3px; }
  .intro { position: absolute; left: 21px; top: 166px; width: 272px; font-size: 17px; line-height: 24px; color: var(--ink); letter-spacing: 0.3px; }

  .field {
    position: absolute; left: 21px; width: 315px; height: 46px;
    background: var(--field-fill); border: 1px solid var(--field-line);
    padding-left: 14px; font: 17px/44px "Questrial", sans-serif; color: var(--placeholder);
  }
  .field-name { top: 284px; }
  .field-email { top: 335px; }
  .field-address { top: 386px; }
  .field-charity { top: 437px; }
  .select-arrow { position: absolute; right: 1px; top: 1px; width: 33px; height: 42px; background: var(--brand-blue); }

  .donate-button {
    position: absolute; left: 210px; top: 509px; width: 123px; height: 45px;
    background: var(--brand-blue); color: #ffffff; border-radius: 2px;
    font: 18px/45px "Questrial", sans-serif; text-align: center;
  }
</style>
</head>
<body>
<div class="page">
  <header class="top-bar">
    <a class="nav-tab nav-faq" href="#">FAQ'S</a>
    <a class="nav-tab nav-charities" href="#">CHARITIES</a>
  </header>

  <div class="hero-photo" role="img" aria-label="Photo of a young boy sitting on concrete steps cradling a sleeping toddler, against a weathered blue wall"></div>

  <div class="slider-dots">
    <span class="slider-dot is-active"></span>
    <span class="slider-dot"></span>
    <span class="slider-dot"></span>
    <span class="slider-dot"></span>
  </div>

  <section class="signup-panel">
    <h1 class="brand-name">giving spark</h1>
    <p class="tagline">its all about charity</p>
    <p class="intro">add our free toolbar and every search you make gives a penny to the charity you love, at no cost to you, so your everyday browsing helps others</p>

    <div class="field field-name">Name</div>
    <div class="field field-email">Email</div>
    <div class="field field-address">Address</div>
    <div class="field field-charity">Charity
      <span class="select-arrow">
        <svg width="33" height="42" viewBox="0 0 33 42"><polygon points="9,15 24,15 16.5,28" fill="#ffffff"/></svg>
      </span>
    </div>

    <div class="donate-button">Donate Now</div>
  </section>
</div>
</body>
</html>
```